Dental x-ray company needs fresh Facebook/Instagram ads

A collection of new ads (single image, carousel, GIF or MP4) for our new campaign. Would like to see optimization for Instagram Story ads as well as creative that can run in Instagram/FB mobile and desktop for FB. Needs to highlight the cost versus our competitors. Open to all formats (single image, carousel, GIF and MP4) as long as the story is conveyed well. The brand is edgier than traditional medical/dental device companies so don't be constrained by the target market typical copy. We are also the only company on the market in the US that offers a unique subscription option so that can be mentioned as well along with the things in the Nice to Have box.

Target Market(s)

Dentists and dental employees

Requirements
Must have
• Our colors:
Orange - ff6319
Teal - 56b1bf
Lt. Teal - aed9da
Blue: #38394B
the KIRA sensor logo
Pic of the KIRA sensor
Tagline: A sensor that makes cents
Nice to have
• I have included a 2 page magazine spread we have recently done, we want in some way to have that comparison table of cost to be in the creative (without the competitor logos)

```html
<!DOCTYPE html>
<html lang="en">
<head>
<meta charset="UTF-8">
<title>A sensor that makes cents</title>
<link rel="stylesheet" href="https://fonts.googleapis.com/css2?family=Archivo+Black&display=swap">
<style>
  :root {
    --brand-orange: #ff6319;
    --brand-blue: #38394b;
    --brand-white: #ffffff;
  }
  * { margin: 0; padding: 0; box-sizing: border-box; }
  html, body {
    width: 960px;
    height: 1200px;
    overflow: hidden;
    background: var(--brand-orange);
  }
  .ad {
    position: relative;
    width: 960px;
    height: 1200px;
    background: var(--brand-orange);
    font-family: "Archivo Black", "Arial Black", sans-serif;
  }
  .tagline { font-weight: 400; }
  .tagline__line {
    position: absolute;
    left: 38px;
    font-size: 190px;
    line-height: 1;
    letter-spacing: -3px;
    text-transform: uppercase;
    white-space: nowrap;
  }
  .tagline__line--light { color: var(--brand-white); }
  .tagline__line--dark { color: var(--brand-blue); letter-spacing: -11px; }
  .tagline__line--1 { top: 48px; }
  .tagline__line--2 { top: 267px; left: 41px; letter-spacing: -1px; }
  .tagline__line--3 { top: 488px; left: 43px; }
  .tagline__line--4 { top: 716px; left: 40px; }
  .tagline__line--5 { top: 923px; left: 39px; }
</style>
</head>
<body>
  <main class="ad">
    <h1 class="tagline" aria-label="A sensor that makes cents">
      <span class="tagline__line tagline__line--light tagline__line--1">A</span>
      <span class="tagline__line tagline__line--light tagline__line--2">Sensor</span>
      <span class="tagline__line tagline__line--light tagline__line--3">That</span>
      <span class="tagline__line tagline__line--dark tagline__line--4">Makes</span>
      <span class="tagline__line tagline__line--dark tagline__line--5">Cents</span>
    </h1>
  </main>
</body>
</html>
```